graphic showing our process of education as a process called a pipeline

Also see my updated comments on discussion section.
Title of the graphic needs to be:
TITLE = The KIVANO Strategic Leadership Pipeline = larger, bold heading
SUB-TITLE = Developing a steady flow of servant leaders for Tanzania's future = under title; smaller font
change the text for each of the 7 steps to match the outcomes listed on the newly attached PDF (strategic pipeline 11x17)
Pipe should be straight or mostly straight.
Pipe should not be in a strong or dark color.
Any icons or symbols should be simple and professional, not like cartoon or childish.
We need a graphic design that shows our PROCESS, called a "pipeline," that is creating future leaders. We are a US-based non-profit that operates a Christian school in rural Tanzania for 600 students (pre-K through 12th grade). It starts with child sponsorship program that allows poor children and orphans to attend school, we have a primary school (like USA elementary school, pre-K thru 7th), and are building a secondary boarding school (like USA middle and high school, grades 8-12), where students will live on campus in dormitories. We offer education, scholarships, leadership development experiences, help finding and securing college scholarships, academic and career counseling, placements for internships and jobs, and networking and leadership development content and events to create the next generation of servant leaders for the country. Prominent colors should probably be the green, blue and black in the Tanzania flag; we want the design to communicate "smart" and "strategic." The stages of the pipeline need to be properly named; we need to show a "leak" in the pipeline after the primary school because we currently have to send our students AWAY to other boarding schools because we don't have one. As the attached recording says, this is bad for their progress. The attached pipeline graphic is very rough and NOT meant to be imitated. It is factually correct, but is busy and not attractive.

Target Market(s)

Major financial contributors and foundations that want to give money to the cause

Industry/Entity Type

non-profit/Christian ministry in education

Font styles to use
Sans Serif

Requirements
Must have
• A "smart" and strategic" feel; preferably visible when on a half page
Nice to have
• a smart, sophisticated, serious look and feel
Should not have
• an elementary school feel

```html
<!DOCTYPE html>
<html lang="en">
<head>
<meta charset="utf-8">
<title>KIVANO Leadership Pipeline</title>
<link href="https://fonts.googleapis.com/css2?family=Montserrat:wght@400;600;700;800&display=swap" rel="stylesheet">
<style>
  :root {
    --blue: #1a9ad6;
    --green: #3ab54a;
    --ink: #141414;
    --pipe: #dedede;
    --paper: #ffffff;
  }
  * { box-sizing: border-box; margin: 0; padding: 0; }
  html, body { width: 1200px; height: 1200px; overflow: hidden; background: var(--paper); }
  .canvas {
    position: relative; width: 1200px; height: 1200px;
    font-family: "Montserrat", Arial, sans-serif; color: var(--ink);
  }
  .title {
    position: absolute; top: 274px; left: 0; width: 1200px; text-align: center;
    font-size: 51px; font-weight: 800; color: var(--blue); letter-spacing: 0.3px;
  }
  .subtitle {
    position: absolute; top: 344px; left: 0; width: 1200px; text-align: center;
    font-size: 24.5px; font-weight: 600; color: var(--ink);
  }
  .rule {
    position: absolute; top: 360px; height: 2px; background: var(--green); width: 84px;
  }
  .rule--left { left: 85px; }
  .rule--right { left: 1022px; }

  .stage { position: absolute; top: 406px; width: 134px; }
  .stage__label {
    height: 75px; background: var(--blue); color: #fff;
    display: flex; align-items: center; justify-content: center; text-align: center;
    font-size: 13.5px; font-weight: 700; line-height: 1.2; text-transform: uppercase; padding: 0 6px;
  }
  .stage__icon {
    width: 60px; height: 60px; margin: 20px auto 0; border-radius: 8px; background: var(--green);
  }
  .stage__link {
    width: 0; height: 72px; margin: 12px auto 0; border-left: 3px dotted var(--blue);
  }
  .stage__link--short { height: 58px; }
  .stage__outcome {
    position: absolute; top: 300px; left: 12px; width: 110px; text-align: center;
    font-size: 11.5px; line-height: 1.15; font-weight: 400;
  }
  .stage__outcome--wide { left: 6px; width: 122px; }

  .pipeline { position: absolute; top: 0; left: 0; }
</style>
</head>
<body>
<main class="canvas">
  <h1 class="title">KIVANO Leadership Pipeline</h1>
  <p class="subtitle">Developing a steady flow of servant leaders for Tanzania</p>
  <span class="rule rule--left"></span>
  <span class="rule rule--right"></span>

  <svg class="pipeline" width="1200" height="1200" viewBox="0 0 1200 1200" aria-hidden="true">
    <rect x="169" y="660" width="1019" height="34" fill="var(--pipe)"/>
    <rect x="165" y="654" width="3" height="46" fill="var(--blue)"/>
    <rect x="172" y="654" width="3" height="46" fill="var(--blue)"/>
    <rect x="1188" y="654" width="3" height="46" fill="var(--blue)"/>
    <rect x="1195" y="654" width="3" height="46" fill="var(--blue)"/>
    <line x1="99" y1="647" x2="143" y2="676" stroke="var(--blue)" stroke-width="3" stroke-dasharray="2 4"/>
    <polygon points="150,681 136,680 144,669" fill="var(--blue)"/>
    <polygon class="leak-crack" points="345,662 354,662 347,675 355,675 339,696 344,681 337,681" fill="var(--blue)"/>
    <path class="leak-drop" d="M337 703 C331 713 327 718 327 723 A10 10 0 0 0 347 723 C347 718 343 713 337 703 Z" fill="none" stroke="var(--blue)" stroke-width="2.5"/>
  </svg>

  <section class="stage" style="left:31px">
    <div class="stage__label">Sponsorship Program</div>
    <div class="stage__icon" role="img" aria-label="Icon of an adult holding a child"></div>
    <div class="stage__link stage__link--short"></div>
    <p class="stage__outcome stage__outcome--wide">Children renewed by spiritual, academic, and health foundations</p>
  </section>
  <section class="stage" style="left:196px">
    <div class="stage__label">Primary School</div>
    <div class="stage__icon" role="img" aria-label="Icon of a young child"></div>
    <div class="stage__link"></div>
    <p class="stage__outcome">Potential leaders with Biblical worldview and strong academic foundations.</p>
  </section>
  <section class="stage" style="left:362px">
    <div class="stage__label">Secondary School</div>
    <div class="stage__icon" role="img" aria-label="Icon of a student beside an atom symbol"></div>
    <div class="stage__link"></div>
    <p class="stage__outcome">Emerging leaders with concrete skills and strong servant mindset.</p>
  </section>
  <section class="stage" style="left:528px">
    <div class="stage__label">Service Leadership Experience</div>
    <div class="stage__icon" role="img" aria-label="Icon of a person helping another up"></div>
    <div class="stage__link"></div>
    <p class="stage__outcome">Growing servant leaders with practical experience to effect change for the kingdom</p>
  </section>
  <section class="stage" style="left:694px">
    <div class="stage__label">Higher Education Support</div>
    <div class="stage__icon" role="img" aria-label="Icon of a graduate in cap and gown"></div>
    <div class="stage__link"></div>
    <p class="stage__outcome">Visionary leaders with expanded capability to solve Tanzania's biggest challenges</p>
  </section>
  <section class="stage" style="left:859px">
    <div class="stage__label">Employment Center</div>
    <div class="stage__icon" role="img" aria-label="Icon of a person walking with a briefcase"></div>
    <div class="stage__link"></div>
    <p class="stage__outcome">Capable Christ-centered leaders in the marketplace as value adding employees and entrepreneurs.</p>
  </section>
  <section class="stage" style="left:1025px">
    <div class="stage__label">Leadership Hub</div>
    <div class="stage__icon" role="img" aria-label="Icon of a large group of people"></div>
    <div class="stage__link"></div>
    <p class="stage__outcome">Mature Christian leaders being placed and positioned for leadership roles in the community and nation.</p>
  </section>
</main>
</body>
</html>
```